Natural Health Supplement Company Needs a Product Label Designed

HARVEST ROOT LABS needs a PROBIOTICS product label designed.We are a natural health vitamin and dietary supplement company. Who ever wins will have the opportunity to design a lot more product labels for us.
Product name: PROBIOTICS
*Please use the attached logo and base the label text exactly off the Kelt Wellness label example.
Other product examples have been attached for inspiration.

Colors

Designer to choose colors to be used in the design.

Requirements
Must have
• Product name: PROBIOTICS
• *Please use the attached logo and base the label text exactly off the Kelt Wellness label example.
• Other product examples have been attached for inspiration.

```html
<!DOCTYPE html>
<html lang="en">
<head>
<meta charset="UTF-8">
<title>Probiotics Label – Harvest Root Labs</title>
<link rel="stylesheet" href="https://fonts.googleapis.com/css2?family=Quicksand:wght@500;700&family=Oswald:wght@700&family=Playfair+Display:ital,wght@1,500&display=swap">
<style>
  :root {
    --leaf-light: #eef5e6;
    --leaf-mid: #cfe3bd;
    --leaf-deep: #a9cc8f;
    --panel: #ffffff;
    --capsule-green: #9cae5a;
    --capsule-light: #c9d396;
    --brown: #6b4a2e;
    --product-green: #4a6a1f;
    --lime: #a8c83a;
    --lime-soft: #cfe07a;
    --badge-grey: #d9ddd2;
    --badge-text: #7d8277;
    --brand-green: #5f8c2a;
  }
  * { margin: 0; padding: 0; box-sizing: border-box; }
  html, body { width: 1200px; height: 800px; overflow: hidden; background: #ffffff; }
  .canvas { position: relative; width: 1200px; height: 800px; overflow: hidden; }
  .backdrop-leaves {
    position: absolute; inset: 0;
    background:
      radial-gradient(ellipse 320px 200px at 160px 150px, var(--leaf-mid), transparent 70%),
      radial-gradient(ellipse 300px 220px at 1040px 420px, var(--leaf-mid), transparent 70%),
      radial-gradient(ellipse 280px 180px at 200px 620px, var(--leaf-deep), transparent 72%),
      radial-gradient(ellipse 260px 180px at 1000px 110px, var(--leaf-mid), transparent 70%),
      radial-gradient(ellipse 260px 160px at 1060px 700px, var(--leaf-mid), transparent 70%),
      var(--leaf-light);
    opacity: 0.8;
  }
  .label-panel {
    position: absolute; left: 348px; top: 38px; width: 502px; height: 724px;
    background: var(--panel);
  }
  .capsule-photo {
    position: absolute; left: 100px; top: 30px; width: 300px; height: 170px;
    background: radial-gradient(ellipse at 50% 60%, var(--capsule-light), var(--capsule-green) 55%, #ffffff 80%);
  }
  .tagline {
    position: absolute; left: 0; top: 226px; width: 100%;
    text-align: center; font-family: "Quicksand", sans-serif; font-weight: 500;
    font-size: 30px; line-height: 40px; color: var(--brown);
  }
  .product-name {
    position: absolute; left: 0; top: 350px; width: 100%;
    text-align: center; font-family: "Oswald", sans-serif; font-weight: 700;
    font-size: 60px; line-height: 76px; letter-spacing: 2px; color: var(--product-green);
  }
  .dosage-badge { position: absolute; left: 318px; top: 432px; width: 150px; height: 130px; }
  .maker-note {
    position: absolute; left: 0; top: 590px; width: 100%;
    text-align: center; font-family: "Playfair Display", serif; font-style: italic;
    font-weight: 500; font-size: 18px; color: var(--brown);
  }
  .brand {
    position: absolute; left: 0; top: 622px; width: 100%;
    display: flex; flex-direction: column; align-items: center; gap: 8px;
  }
  .brand-dot { width: 34px; height: 34px; border-radius: 50%; background: var(--brand-green); }
  .brand-name {
    font-family: "Quicksand", sans-serif; font-weight: 700; font-size: 32px;
    letter-spacing: 1px; color: var(--brand-green);
  }
</style>
</head>
<body>
<div class="canvas">
  <div class="backdrop-leaves" role="img" aria-label="Soft faded photograph of fresh green leaves"></div>

  <section class="label-panel">
    <div class="capsule-photo" role="img" aria-label="Photo of green herbal capsules with a pile of green powder"></div>

    <p class="tagline">Natural Way to Balance<br>Your Digestive System</p>

    <h1 class="product-name">PROBIOTICS</h1>

    <svg class="dosage-badge" viewBox="0 0 150 130" aria-label="Once daily">
      <defs>
        <linearGradient id="badgeFill" x1="0" y1="0" x2="1" y2="1">
          <stop offset="0" stop-color="#eef0ea"/>
          <stop offset="1" stop-color="var(--badge-grey)"/>
        </linearGradient>
      </defs>
      <circle cx="66" cy="68" r="52" fill="url(#badgeFill)"/>
      <circle cx="124" cy="42" r="12" fill="var(--lime-soft)"/>
      <circle cx="112" cy="100" r="16" fill="var(--lime)"/>
      <circle cx="134" cy="74" r="7" fill="var(--lime-soft)"/>
      <text x="68" y="64" text-anchor="middle" font-family="Quicksand, sans-serif" font-weight="700" font-size="30" fill="var(--lime)">Once</text>
      <text x="70" y="92" text-anchor="middle" font-family="Quicksand, sans-serif" font-weight="700" font-size="18" fill="var(--badge-text)">Daily</text>
    </svg>

    <p class="maker-note">Manufactured By</p>

    <div class="brand">
      <span class="brand-dot" aria-hidden="true"></span>
      <span class="brand-name">HARVEST ROOT LABS</span>
    </div>
  </section>
</div>
</body>
</html>
```